RZO Design tag

Looking to design a tag for our new hat & glove brand RZO Design. These are winter hats & gloves. Long story short these are lower cost/retail items but I'm trying to convey higher quality goods through a nice tag. I’ve attached a tag of another brand we have to give you a general idea of what I’d be looking for- but again for our new brand RZO Design.
I’m thinking we can do one general design- and then do it in 4 different color schemes: First one mimicking the attachment’s colors for ladies items- so a few different shades of pink. Then 2nd color scheme a darker more masculine color tone for mens or unisex items- maybe blue/dark blue, and then a 3rd color scheme for kids items that is more vibrant/kid like colors. Last one red & green for some Christmas items we do.
A few things:
• Trying to make the tags look classy as possible
• The tag will need to measure 2.25” high x 2” wide. The top little bit would have to be space left blank for a hole punch- just like on the attached sample tag. But again the tags designed would need to be 2.25" tall x 2" wide so not the same shape as the sample tag.
• For item name you can just put “Knit Hat” for the generic tag item name (in place of what says on the same “Chenille Slipper Bootie”). Please try to keep the writing a nice font similar to what is on this tag- again trying to have a classy tag look
• On the bottom center (In place of Made in China) it would just need to say “One Size” in standard font
Hope this helps & thank you
Target Market(s)
People buying winter hats & gloves
Industry/Entity Type
Retail- winter hats & gloves
Look and feel

```html
<!DOCTYPE html>
<html lang="en">
<head>
<meta charset="utf-8">
<title>Knit Hat Tags</title>
<link rel="stylesheet" href="https://fonts.googleapis.com/css2?family=Yellowtail&family=Montserrat:wght@500&display=swap">
<style>
  :root {
    --page-bg: #ffffff;
    --lettering: #ffffff;
    --hole: #f2f2f2;
    --pink-light: #f28cfc;
    --pink-mid: #d466fb;
    --pink-shadow: #e83ee8;
    --pink-band: #ff00ff;
    --blue-light: #2a7bff;
    --blue-mid: #0a4bff;
    --blue-shadow: #0000cc;
    --blue-band: #000b80;
    --kids-light: #fdbd2a;
    --kids-mid: #fa9703;
    --kids-shadow: #ff6a00;
    --kids-band: #ff4a0a;
    --xmas-light: #ff0000;
    --xmas-mid: #b30000;
    --xmas-shadow: #0d7a00;
    --xmas-band: #44ff14;
  }
  * { margin: 0; padding: 0; box-sizing: border-box; }
  html, body {
    width: 1200px;
    height: 1000px;
    overflow: hidden;
    background: var(--page-bg);
  }
  .sheet {
    position: relative;
    width: 1200px;
    height: 1000px;
  }
  .tag {
    position: absolute;
    width: 365px;
    height: 410px;
    overflow: hidden;
    box-shadow: 0 1px 3px rgba(0,0,0,0.18);
  }
  .tag--ladies { left: 181px; top: 35px;
    --light: var(--pink-light); --mid: var(--pink-mid); --shadow: var(--pink-shadow); --band: var(--pink-band); }
  .tag--mens { left: 660px; top: 35px;
    --light: var(--blue-light); --mid: var(--blue-mid); --shadow: var(--blue-shadow); --band: var(--blue-band); }
  .tag--kids { left: 181px; top: 559px;
    --light: var(--kids-light); --mid: var(--kids-mid); --shadow: var(--kids-shadow); --band: var(--kids-band); }
  .tag--holiday { left: 660px; top: 559px;
    --light: var(--xmas-light); --mid: var(--xmas-mid); --shadow: var(--xmas-shadow); --band: var(--xmas-band); }

  .tag__pattern {
    position: absolute;
    inset: 0;
    background: linear-gradient(160deg, var(--light) 0%, var(--mid) 45%, var(--light) 70%, var(--mid) 100%);
  }
  .tag__hole {
    position: absolute;
    left: 171px;
    top: 37px;
    width: 22px;
    height: 22px;
    border-radius: 50%;
    background: var(--hole);
  }
  .tag__name {
    position: absolute;
    font-family: "Yellowtail", cursive;
    font-size: 118px;
    color: var(--lettering);
    text-shadow: 4px 3px 0 var(--shadow);
    line-height: 1;
    white-space: nowrap;
    transform: rotate(-4deg);
    transform-origin: left bottom;
  }
  .tag__name--first {
    left: 62px;
    top: 100px;
  }
  .tag__name--second {
    left: 46px;
    top: 208px;
  }
  .tag__size {
    position: absolute;
    left: 103px;
    top: 341px;
    width: 159px;
    height: 23px;
    background: var(--band);
    color: var(--lettering);
    font-family: "Montserrat", sans-serif;
    font-weight: 500;
    font-size: 21px;
    line-height: 23px;
    text-align: center;
    letter-spacing: 0.5px;
  }
</style>
</head>
<body>
<main class="sheet">
  <section class="tag tag--ladies">
    <div class="tag__pattern" role="img" aria-label="Decorative pattern of overlapping rounded blocks in pink shades"></div>
    <span class="tag__hole"></span>
    <p class="tag__name tag__name--first">Knit</p>
    <p class="tag__name tag__name--second">Hat</p>
    <p class="tag__size">one size</p>
  </section>

  <section class="tag tag--mens">
    <div class="tag__pattern" role="img" aria-label="Decorative pattern of overlapping rounded blocks in blue shades"></div>
    <span class="tag__hole"></span>
    <p class="tag__name tag__name--first">Knit</p>
    <p class="tag__name tag__name--second">Hat</p>
    <p class="tag__size">one size</p>
  </section>

  <section class="tag tag--kids">
    <div class="tag__pattern" role="img" aria-label="Decorative pattern of overlapping rounded blocks in orange and yellow shades"></div>
    <span class="tag__hole"></span>
    <p class="tag__name tag__name--first">Knit</p>
    <p class="tag__name tag__name--second">Hat</p>
    <p class="tag__size">one size</p>
  </section>

  <section class="tag tag--holiday">
    <div class="tag__pattern" role="img" aria-label="Decorative pattern of overlapping rounded blocks in red shades"></div>
    <span class="tag__hole"></span>
    <p class="tag__name tag__name--first">Knit</p>
    <p class="tag__name tag__name--second">Hat</p>
    <p class="tag__size">one size</p>
  </section>
</main>
</body>
</html>
```